58 Restaurant & Bar Menu

Want to make current menu more trendy in design. I have attached a pdf of the menu and of the logo. Rather, than being 6 pages I would like to make the menu into "4 pages". The menu will be printed in color.

I am open to designs that will allow the menu to be printed on 11x17 paper that will be folded in half. The "Breakfast" section needs to be its own page and all the way on the back.

As for the cover I am open to just keeping it as a cover with the info I have on it but completely different design/picture change. The logo needs to stay. The cover can also be used as having menu items on there if pulled of correctly.

The readability has to be clear to the guests.

The restaurant is a Mediterranean style and for the area it is priced mid-high. The atmosphere is casual fine dining with Martini & Wine Bar. All are ingredients are fresh never frozen and everything is prepared from scratch.

Industry/Entity Type

Restaurant

Requirements
Must have
• Breakfast on its own page on the back.
Nice to have
• Trendy Design

```html
<!DOCTYPE html>
<html lang="en">
<head>
<meta charset="utf-8">
<title>58 Restaurant &amp; Bar – Breakfast Menu</title>
<link rel="stylesheet" href="https://fonts.googleapis.com/css2?family=Lora:ital,wght@1,600;1,700&family=Mulish:ital,wght@0,700;0,800;1,400&display=swap">
<style>
:root{
  --ink:#161616;
  --aqua:#6fdde6;
  --aqua-line:#c3eff3;
  --panel-a:#eef9f7;
  --panel-b:#d3f0ea;
  --paper:#ffffff;
  --sans:"Mulish", Arial, sans-serif;
  --serif:"Lora", Georgia, serif;
}
*{box-sizing:border-box;margin:0;padding:0}
html,body{width:1200px;height:776px;overflow:hidden;background:var(--paper)}
.sheet{position:relative;width:1200px;height:776px;overflow:hidden;background:var(--paper);color:var(--ink);font-family:var(--sans)}
.abs{position:absolute}

/* plain lines and info panel */
.stripe{position:absolute;top:0;height:776px;background:var(--aqua-line)}
.band{position:absolute;height:6px;background:#eaf6f7}
.info-panel{position:absolute;left:652px;top:470px;width:480px;height:212px;border-radius:70px 0 34px 34px;background:linear-gradient(135deg,var(--panel-a),var(--panel-b))}

/* back page */
.page-title{left:200px;top:28px;width:244px;text-align:center;font:800 21px/1 var(--sans)}
.page-sub{left:180px;top:54px;width:284px;text-align:center;font:700 italic 12px/1 var(--serif)}
.section-title{font:700 italic 16px/1 var(--serif)}
.item{font:800 10.5px/14px var(--sans)}
.item.feature{color:var(--aqua)}
.desc{font:400 italic 7px/11px var(--sans);margin-bottom:1px}
.desc.feature{color:var(--aqua)}
.photo{position:absolute;border-radius:4px}

/* cover */
.brand{left:690px;top:146px;display:flex;align-items:center;gap:14px}
.brand-dot{width:52px;height:52px;border-radius:50%;background:var(--aqua)}
.brand-name{font:800 32px/1 var(--sans);color:var(--ink)}
.cover-info{left:660px;top:500px;width:400px;text-align:center;font:700 italic 15px/25.7px var(--serif)}
.cover-info .accent{color:var(--aqua)}
</style>
</head>
<body>
<div class="sheet">

  <div class="band" style="left:600px;top:18px;width:540px" aria-hidden="true"></div>
  <div class="stripe" style="left:1142px;width:6px" aria-hidden="true"></div>
  <div class="stripe" style="left:1156px;width:4px" aria-hidden="true"></div>
  <div class="info-panel" aria-hidden="true"></div>

  <!-- BACK PAGE: BREAKFAST -->
  <h1 class="abs page-title">Breakfast</h1>
  <p class="abs page-sub">Served Saturday &amp; Sunday</p>

  <section class="abs" style="left:74px;top:82px;width:152px">
    <h2 class="section-title" style="margin-left:42px;margin-bottom:5px">Skillets</h2>
    <p class="item">Veggie $6.95</p>
    <p class="desc">Skillet full of hash browns, onions, peppers, tomatoes &amp; mushrooms topped with cheese and 2 eggs. Served w/ Toast.</p>
    <p class="item">Irish $7.95</p>
    <p class="desc">Skillet full of hash browns, onions, peppers &amp; mushrooms topped with cheese and 2 eggs. Served w/ Toast.</p>
    <p class="item">Melting Pot $8.95</p>
    <p class="desc">Skillet full of hash browns, ham, bacon, sausage, mushrooms, onions, tomatoes and peppers topped with cheese and 2 eggs. Served with toast.</p>
    <p class="item feature">Biscuits &amp; Gravy $7.95</p>
    <p class="desc feature">Skillet full of hash browns, onions, peppers &amp; cheese. Topped w/ homemade biscuit, sausage gravy &amp; 2 eggs.</p>
  </section>

  <div class="photo" role="img" aria-label="Photo of steak and eggs with asparagus" style="left:252px;top:124px;width:145px;height:74px;background:linear-gradient(135deg,#3c5a2a,#6a3b22 45%,#f2c04a 80%,#fff)"></div>
  <div class="photo" role="img" aria-label="Photo of a vegetable omelette with toast" style="left:252px;top:222px;width:144px;height:82px;background:linear-gradient(135deg,#8a5a30,#e8cf6a 45%,#f1e6a0 70%,#ececec)"></div>

  <section class="abs" style="left:418px;top:82px;width:150px">
    <h2 class="section-title" style="margin-left:38px;margin-bottom:9px">Omelettes</h2>
    <p class="desc" style="font-size:8.5px;line-height:12px;text-align:center;margin-bottom:10px;width:170px">Fluffy Pan-Fried Omelettes,<br>Served w/ Hash Browns &amp; Toast</p>
    <p class="item">Athenian $8.95</p>
    <p class="desc">Gyro off-the-cone, tomatoes, onions, olives, &amp; feta cheese.<br>Served with side of homemade cucumber sauce.</p>
    <p class="item">Denver $7.95</p>
    <p class="desc">Ham, onion, pepper &amp; cheese.</p>
    <p class="item">Veggie $7.95</p>
    <p class="desc">Onions, peppers, tomatoes &amp; mushrooms</p>
    <p class="item">Deluxe $8.95</p>
    <p class="desc">Ham, bacon, sausage, mushrooms, onions, tomatoes &amp;<br>peppers.</p>
    <p class="item feature">Spinach Pesto $8.95</p>
    <p class="desc feature">Sun-Dried tomatoes, spinach, mushrooms &amp; cheese.<br>Topped w/ Pesto Cream Sauce.</p>
    <p class="item">Ham &amp; Cheese $6.95</p>
  </section>

  <section class="abs" style="left:74px;top:338px;width:205px">
    <h2 class="section-title" style="margin-bottom:7px">Eggs &amp; Specialties</h2>
    <p class="item">Two Eggs, Hash Browns &amp; Toast $4.95</p>
    <p class="item">With Bacon, Sausage or Ham $5.95</p>
    <p class="item">With Corned Beef Hash $6.55</p>
    <p class="item">With Gyro off-the-cone $6.95</p>
    <p class="item">Steak &amp; Eggs $13.95</p>
    <p class="desc">8oz Prime Cut Steak, 2 Eggs, hash browns, &amp; Toast.</p>
    <p class="item">Chop Steak &amp; Eggs $9.95</p>
    <p class="desc">10oz Chopped Sirloin Steak, 2 Eggs, hash browns, &amp; Toast.</p>
    <p class="item">Granny’s Breakfast $6.95</p>
    <p class="desc">Two Eggs scrambled w/ potatoes, ham, onions &amp; peppers topped w/ cheese. Served with toast.</p>
    <p class="item">3 Deuces $6.95</p>
    <p class="desc">Two Eggs, Two Pancakes &amp; Two Sausage Links or Bacon Strips.</p>
    <p class="item">Homemade Biscuits &amp; Gravy</p>
    <p class="item">Half $3.95 / Full $5.55</p>
  </section>

  <section class="abs" style="left:360px;top:452px;width:215px">
    <h2 class="section-title" style="margin-left:22px;margin-bottom:11px">Light Breakfast</h2>
    <p class="item">Egg, Sausage, &amp; Cheese Sand. $4.25</p>
    <p class="item">Oatmeal or Cereal $3.55 w/ raisins $3.95</p>
    <p class="item">Bagel w/ cream cheese $2.55</p>
    <p class="item">English Muffin or Raisin Toast $1.55</p>
    <p class="item feature">Mediterranean Pita $6.95</p>
    <p class="desc feature">Pesto Spread on Pita Bread w/ tomatoes, spinach, feta &amp; an Egg</p>
    <p class="item">Fresh Fruit Bowl $4.95</p>
  </section>

  <section class="abs" style="left:150px;top:634px;width:280px">
    <h2 class="section-title" style="margin-bottom:13px">Pancakes, French Toast &amp; Waffles</h2>
    <p class="item">Apple Danish French Toast $6.95</p>
    <p class="item">Bananas Foster Pancakes $7.95</p>
    <p class="item">Strawberry Cake Waffle $7.95</p>
    <p class="item">Pancakes or French Toast (2) $4.55 / (3) $4.95</p>
    <p class="item">Belgium Waffle $4.95</p>
    <p class="item">Add Fruit Topping, Bacon, Ham or Sausage $1.95</p>
  </section>

  <div class="photo" role="img" aria-label="Photo of crepes with chocolate drizzle and strawberries" style="left:432px;top:668px;width:145px;height:85px;background:linear-gradient(135deg,#f4f0ea,#e2b77a 45%,#5a3320 70%,#d9434a)"></div>

  <!-- FRONT COVER -->
  <div class="abs brand">
    <span class="brand-dot" aria-hidden="true"></span>
    <span class="brand-name">58 Restaurant &amp; Bar</span>
  </div>

  <address class="abs cover-info">
    <p>48 S Lakeview Ave. Millbrook, WI 53990</p>
    <p>262-555-0158</p>
    <p>www.58restaurant.com</p>
    <p class="accent">Serving Breakfast Saturday &amp; Sunday</p>
    <p>Catering &amp; Private Party Hosting Available</p>
    <p>Friday Fish Fry - Saturday Prime Rib</p>
  </address>

</div>
</body>
</html>
```